church business card design

we have a logo and would like our business card to complement the logo. we would prefer the logo in white on a coloured background - probably blue. Under the logo or near it we would have the Words 'Love God. Love people. Follow Jesus.'
We would like some yellow/gold highlights. We like the design by marlow inkworks 88 front of card - https://www.pitchvelta.com/businesscard-design/contest/5182094

Our church is multicultural, inner city, friendly, warm welcoming and that's the feel we would like. there's also an element of being spontaneous, so a swirl or swoosh might help give that feel. the example card above had some curved shapes on the front of the card for example.
on the second side of the card would have the details of the Senior Pastor and the contact details for the church.
after the business card we would be looking at letterhead and an A5 flyer for printing but also as document templates so we can create invitations etc going forward

```html
<!DOCTYPE html>
<html lang="en">
<head>
<meta charset="utf-8">
<title>Harbor Stone Church – Business Card</title>
<link rel="stylesheet" href="https://fonts.googleapis.com/css2?family=Montserrat:wght@400;500;700&display=swap">
<style>
  :root {
    --navy: #0e1140;
    --navy-deep: #0a0c33;
    --gold: #e0a81e;
    --white: #ffffff;
    --silver: #c7cad3;
    --backdrop: #dcdcdc;
  }
  * { box-sizing: border-box; margin: 0; padding: 0; }
  html, body { width: 1200px; height: 800px; overflow: hidden; }
  body {
    background: var(--backdrop);
    font-family: "Montserrat", Arial, sans-serif;
    display: flex;
    align-items: center;
    justify-content: center;
    gap: 40px;
  }
  .card {
    position: relative;
    width: 540px;
    height: 309px;
    border-radius: 22px;
    background: linear-gradient(160deg, var(--navy) 0%, var(--navy-deep) 100%);
    border: 2px solid var(--gold);
    overflow: hidden;
    color: var(--white);
  }
  .logo-block {
    position: absolute;
    display: flex;
    flex-direction: column;
    align-items: flex-start;
  }
  .church-name {
    font-weight: 700;
    letter-spacing: 0.5px;
    line-height: 1.05;
  }
  .tagline {
    border-top: 1px solid var(--gold);
    padding-top: 5px;
    margin-top: 8px;
    font-weight: 500;
    white-space: nowrap;
  }
  /* details side */
  .card--details .logo-block { left: 30px; top: 108px; }
  .card--details .church-name { font-size: 30px; color: var(--white); }
  .card--details .tagline { font-size: 11.5px; color: var(--gold); }
  .divider {
    position: absolute;
    left: 262px; top: 40px;
    width: 1px; height: 230px;
    background: linear-gradient(to bottom, transparent, rgba(255,255,255,0.35), transparent);
  }
  .contact { position: absolute; left: 290px; top: 52px; }
  .contact__name { font-size: 19px; font-weight: 700; letter-spacing: 0.5px; text-transform: uppercase; }
  .contact__role { font-size: 14px; color: var(--gold); font-weight: 500; margin-bottom: 12px; }
  .contact__address { font-size: 11.5px; line-height: 1.5; margin-bottom: 10px; }
  .contact__list { list-style: none; font-size: 11.5px; line-height: 1.7; }
  .contact__list li { display: flex; align-items: center; gap: 8px; }
  .contact__list svg { width: 12px; height: 12px; fill: var(--gold); flex: none; }
  /* logo side */
  .card--logo .logo-block { left: 50%; top: 50%; transform: translate(-50%, -50%); align-items: center; }
  .card--logo .church-name { font-size: 40px; color: var(--silver); }
  .card--logo .tagline { font-size: 15px; color: var(--silver); border-top-color: var(--silver); padding-top: 7px; }
</style>
</head>
<body>
  <section class="card card--details">
    <div class="logo-block">
      <p class="church-name">Harbor Stone<br>Church</p>
      <p class="tagline">Love God • Love people • Follow Jesus</p>
    </div>
    <div class="divider"></div>
    <div class="contact">
      <p class="contact__name">Daniel Okafor</p>
      <p class="contact__role">Senior Pastor</p>
      <p class="contact__address">4120 Willow Bend Road<br>Fairbanks, Alaska 99712</p>
      <ul class="contact__list">
        <li><svg viewBox="0 0 24 24"><path d="M6.6 10.8a15.1 15.1 0 0 0 6.6 6.6l2.2-2.2c.3-.3.7-.4 1-.2 1.1.4 2.3.6 3.6.6.6 0 1 .4 1 1V20c0 .6-.4 1-1 1A17 17 0 0 1 3 4c0-.6.4-1 1-1h3.5c.6 0 1 .4 1 1 0 1.3.2 2.5.6 3.6.1.3 0 .7-.2 1z"/></svg>555-201-4478</li>
        <li><svg viewBox="0 0 24 24"><path d="M6 2h12v5H6zM3 8h18a1 1 0 0 1 1 1v8h-4v5H6v-5H2V9a1 1 0 0 1 1-1zm5 7v5h8v-5z"/></svg>555-201-4479</li>
        <li><svg viewBox="0 0 24 24"><path d="M2 5h20v14H2zm2 2v.5l8 5 8-5V7zm0 2.8V17h16V9.8l-8 5z"/></svg>hello@harborstone.org</li>
        <li><svg viewBox="0 0 24 24"><path d="M12 2a10 10 0 1 0 0 20 10 10 0 0 0 0-20zm6.9 9h-3a15 15 0 0 0-1.3-6A8 8 0 0 1 18.9 11zM12 4.1c.9 1.2 1.7 3.7 1.9 6.9h-3.8c.2-3.2 1-5.7 1.9-6.9zM9.4 5a15 15 0 0 0-1.3 6h-3A8 8 0 0 1 9.4 5zm-4.3 8h3a15 15 0 0 0 1.3 6A8 8 0 0 1 5.1 13zm6.9 6.9c-.9-1.2-1.7-3.7-1.9-6.9h3.8c-.2 3.2-1 5.7-1.9 6.9zm2.6-.9a15 15 0 0 0 1.3-6h3a8 8 0 0 1-4.3 6z"/></svg>www.harborstone.org</li>
      </ul>
    </div>
  </section>

  <section class="card card--logo">
    <div class="logo-block">
      <p class="church-name">Harbor Stone Church</p>
      <p class="tagline">Love God • Love people • Follow Jesus</p>
    </div>
  </section>
</body>
</html>
```